Wordpress Design Project

We are a local restaurant who needs a quality online identity base. We operate in a 1930's Villa, and our target market is the below mid - upper. Our main sale is the evening dinner meal, while we also sell home-made goods, including preserves, and handmade chocolates.
The final Wordpress coded design will:
Be a base for information including Contact details, and a Map of it's location. It will also include photographs of some of the dishes to give an idea to potential customers as to the style and target market.
The site will have 4 main pages
-Main
-About
-Menu
-Contact
Ideas for elements we would like to have included in the design are
Cardboard tags with the links to the other pages, which give a home-made feel
Character wood, with deep grain to emphasis our homely feel
An 'aged' map of the location. Possibly on a large cardboard tag.
Link to our Linkbook page
Link to our Plate Finder review page http://www.platefinder.co.nz/restaurant.php?rest=4720
Notes:
The final Wordpress site should communicate a homely inviting image, with deep character, while still looking elegant and slightly simplistic. We would like fine fonts, with nice spacing, especially on the cardboard tags.
I have attached a mockup of our very loose vision for the site to give you an idea of the line we would like to go down. This is just for initial ideas, and we are happy for radically different designs, or just neat variations on the base design
Professional, edited photos of the food available will be uploaded alongside this project
Villa Marrow does not have an official Logo for use on the website, so a simple header that ties in with the page will be fine. This may be replaced eventually with a new logo
Address and Hosting is already setup with the address being www.villamarrowkitchen.co.nz with a placeholder site online.
We look forward to all designs, and welcome any questions. This should be an nice job for someone with an eye for detail.

```html
<!DOCTYPE html>
<html lang="en">
<head>
<meta charset="utf-8">
<title>Villa Marrow</title>
<link rel="stylesheet" href="https://fonts.googleapis.com/css2?family=Pinyon+Script&family=PT+Sans:wght@400;700&display=swap">
<style>
:root{
  --wood-dark:#4a1f0c;
  --wood-mid:#6b2f14;
  --paper:#e4e3e1;
  --ink:#4a2616;
  --brown:#5a2a12;
  --brown-deep:#3d1a09;
  --tag:#e9dcc4;
  --tag-edge:#c9b69a;
  --string:#8a7a66;
  --line:#9a968f;
  --board:#2a2620;
  --chalk-text:#e6e2d6;
  --cream:#fff;
}
*{box-sizing:border-box;margin:0;padding:0}
html,body{width:863px;height:1200px;overflow:hidden}
body{font-family:"PT Sans",sans-serif;color:var(--ink);position:relative}
.wood{position:absolute;inset:0;background:linear-gradient(100deg,var(--wood-dark),var(--wood-mid) 45%,var(--wood-dark))}
.sheet{position:absolute;left:84px;top:35px;width:699px;height:1120px;background:var(--paper);border-radius:12px;box-shadow:0 2px 10px rgba(0,0,0,.45)}
.abs{position:absolute}
.script{font-family:"Pinyon Script",cursive}
.brand{left:26px;top:22px;font-size:37px;line-height:1;color:var(--ink)}
.tagline{left:34px;top:58px;font-size:15px;color:var(--ink)}
.phone{right:33px;top:40px;font-size:16px;color:var(--ink)}
.social{right:33px;top:60px;display:flex;gap:8px;font-size:10px;color:var(--ink)}
.social span{display:flex;align-items:center;gap:3px}
.social i{width:8px;height:8px;background:var(--brown);display:inline-block}
.nav{left:0;top:103px;width:699px;height:50px}
.nav-tag{position:absolute;top:0;width:76px;height:46px;background:var(--tag);border:1px solid var(--tag-edge);clip-path:polygon(9px 0,100% 0,100% 100%,9px 100%,0 50%);box-shadow:2px 3px 4px rgba(0,0,0,.25);display:flex;align-items:center;justify-content:center;font-size:13px;color:var(--ink);text-decoration:none}
.nav-tag.current{color:var(--cream)}
.slider{left:45px;top:169px;width:605px;height:205px;background:#c9c4bd;box-shadow:0 3px 6px rgba(0,0,0,.3)}
.slide-photo{left:7px;top:6px;width:591px;height:194px;background:radial-gradient(ellipse at 60% 40%,#8a5a2a,#3a200d 55%,#160a03)}
.slide-url{left:7px;top:23px;width:591px;height:58px;background:rgba(40,20,8,.55);color:var(--cream);font-size:27px;padding:12px 12px}
.dots{left:283px;top:178px;display:flex;gap:4px}
.dots i{width:10px;height:10px;border-radius:50%;background:var(--cream)}
.dots i:first-child{background:var(--brown-deep)}
.arrow{top:244px}
.divider{left:40px;width:620px;height:3px;border-top:1px solid var(--line);border-bottom:1px solid #fff}
.section-title{left:0;width:699px;text-align:center;font-size:40px;font-weight:400;color:var(--ink)}
.card{top:476px;width:198px;height:142px;background:linear-gradient(180deg,var(--brown),var(--brown-deep));box-shadow:0 4px 8px rgba(0,0,0,.3)}
.card-title{height:30px;text-align:center;color:var(--cream);font-size:20px;line-height:32px}
.card-photo{height:78px;background:radial-gradient(ellipse at 50% 75%,#f1ece2 0 35%,#7a4a22 60%,#2a1406)}
.card-foot{height:34px;position:relative}
.more{position:absolute;left:10px;top:7px;width:36px;height:19px;background:var(--tag);clip-path:polygon(5px 0,100% 0,100% 100%,5px 100%,0 50%);font-size:11px;line-height:19px;padding-left:6px;color:var(--ink)}
.price{position:absolute;right:10px;top:7px;color:var(--cream);font-size:16px}
.price sup{font-size:9px}
.news{left:54px;top:716px;width:451px;height:104px;background:linear-gradient(90deg,rgba(90,42,18,0),#7a4a2a 45%,var(--brown))}
.news-text{right:132px;top:10px;text-align:right;color:var(--cream)}
.news-text b{display:block;font-size:19px}
.news-text span{display:block;font-size:19px;line-height:1}
.news-text small{display:block;font-size:9px;margin-top:5px}
.news-read{right:139px;top:68px;width:60px;height:26px;background:var(--tag);clip-path:polygon(6px 0,100% 0,100% 100%,6px 100%,0 50%);font-size:10px;line-height:26px;padding-left:9px;color:var(--ink);white-space:nowrap}
.news-photo{right:3px;top:3px;width:117px;height:98px;background:radial-gradient(ellipse at 40% 50%,#b56a4a,#6a3a1c 55%,#c9b07a)}
.board{left:506px;top:649px;width:163px;height:238px;background:var(--board);border-radius:6px;color:var(--chalk-text);padding:42px 13px 0}
.board h3{font-family:"Pinyon Script",cursive;font-weight:400;font-size:14px;margin-bottom:16px}
.board p{font-size:8.5px;line-height:11.4px;white-space:nowrap}
.welcome-text{left:32px;top:990px;width:640px;font-size:12.5px;line-height:16.5px;letter-spacing:-.2px;color:var(--ink)}
.read-more{left:313px;top:1055px;width:65px;height:37px;background:var(--tag);clip-path:polygon(8px 0,100% 0,100% 100%,8px 100%,0 50%);box-shadow:2px 3px 4px rgba(0,0,0,.25);font-size:12px;line-height:37px;padding-left:12px;color:var(--ink);white-space:nowrap}
svg.string{position:absolute;overflow:visible}
</style>
</head>
<body>
<div class="wood" role="img" aria-label="Deep-grain dark wood background"></div>
<main class="sheet">
  <header>
    <div class="abs brand script">Villa Marrow</div>
    <div class="abs tagline script">We operate in a 1930's Villa</div>
    <div class="abs phone script">Phone : 03 555 0148</div>
    <div class="abs social"><span><i></i>Linkbook</span><span><i></i>Plate Finder</span></div>
  </header>

  <nav class="abs nav">
    <svg class="string" width="699" height="50"><path d="M190 26 Q222 32 250 26 M322 26 Q354 32 382 26 M454 26 Q486 32 515 26" stroke="var(--string)" stroke-width="1.5" fill="none"/></svg>
    <a class="nav-tag current" style="left:115px">Home</a>
    <a class="nav-tag" style="left:247px">About Us</a>
    <a class="nav-tag" style="left:379px">Menu</a>
    <a class="nav-tag" style="left:512px">Contact</a>
  </nav>

  <section class="abs slider">
    <div class="abs slide-photo" role="img" aria-label="Candlelit dinner table with wine glasses and a menu"></div>
    <div class="abs slide-url script">www.villamarrowkitchen.co.nz</div>
    <div class="abs dots"><i></i><i></i><i></i><i></i></div>
  </section>
  <svg class="abs arrow" style="left:18px" width="27" height="55"><path d="M27 0 V55 L0 27 Z" fill="var(--brown-deep)"/><path d="M16 20 L10 27 L16 34" stroke="#fff" stroke-width="2.5" fill="none"/></svg>
  <svg class="abs arrow" style="left:650px" width="27" height="55"><path d="M0 0 V55 L27 27 Z" fill="var(--brown-deep)"/><path d="M10 20 L16 27 L10 34" stroke="#fff" stroke-width="2.5" fill="none"/></svg>

  <div class="abs divider" style="top:388px"></div>
  <h2 class="abs section-title script" style="top:402px">Evening Dinner Meals</h2>
  <div class="abs divider" style="top:457px"></div>

  <article class="abs card" style="left:17px">
    <div class="card-title script">Handmade Chocolates</div>
    <div class="card-photo" role="img" aria-label="Plated dessert with berries"></div>
    <div class="card-foot"><span class="more script">More</span><span class="price">£ 37.<sup>50</sup></span></div>
  </article>
  <article class="abs card" style="left:250px">
    <div class="card-title script">Handmade Chocolates</div>
    <div class="card-photo" role="img" aria-label="Plated main course with greens"></div>
    <div class="card-foot"><span class="more script">More</span><span class="price">£ 37.<sup>50</sup></span></div>
  </article>
  <article class="abs card" style="left:482px">
    <div class="card-title script">Handmade Chocolates</div>
    <div class="card-photo" role="img" aria-label="Chocolate pudding with ice cream"></div>
    <div class="card-foot"><span class="more script">More</span><span class="price">£ 37.<sup>50</sup></span></div>
  </article>

  <section class="abs news">
    <div class="abs news-text"><b>News</b><span>evening dinner meal</span><small>ON ORDEES OVER <b style="display:inline;font-size:9px">£ 99.99</b></small></div>
    <svg class="string" style="left:212px;top:78px" width="95" height="10"><path d="M0 4 Q45 10 92 4" stroke="var(--string)" stroke-width="1.5" fill="none"/></svg>
    <div class="abs news-read script">Read More</div>
    <div class="abs news-photo" role="img" aria-label="Jars of homemade preserves with tags"></div>
  </section>

  <aside class="abs board" role="img" aria-label="Chalkboard easel with location and opening details">
    <h3>14 Tarrant Lane Gore</h3>
    <p>Region: Southland<br>Licence: Fully Licensed<br>Cuisine: A La Carte<br>Phone : 03 555 0148<br>Email:&nbsp; info@villamarrow.co.nz<br>Open<br>Tuesday till Saturday from 5.30<br>untill late</p>
  </aside>

  <div class="abs divider" style="top:917px"></div>
  <h2 class="abs section-title script" style="top:932px">Welcome to Villa Marrow</h2>
  <p class="abs welcome-text">Our friendly, local business has been operating in Notown, UK for many years. We have an experienced and disciplined team who can take on any task, regardless of size, here in Notown UK. We pride ourselves on our impeccably high standards and always strive to deliver in a way that suits your schedule and budget.</p>
  <svg class="string" style="left:258px;top:1068px" width="60" height="12"><path d="M0 6 Q30 0 58 6" stroke="var(--string)" stroke-width="1.5" fill="none"/></svg>
  <div class="abs read-more script">Read More</div>
</main>
</body>
</html>
```